professional business card design

Business card design. Photos have been uploaded and i am open to the designer choosing which photos to use. Would like the card to be mostyly in a grey scale design with black, whites, silver & grey colours. I have added copy of our flyer as would like on the back side of card our services to be listed. Do not use any bright colurs such as blue red green or yellow. i need to be able to edit the phone number and naem in the final card design submitted.

Target Market(s)

Clients

Industry/Entity Type

earhmovibng and transport

Contact Information for Business Card

Director Name, address, email, phone number and services

Colors

Designer to choose only greyscale colors for use in the design.

Requirements
Should not have
• no yellow, red, blue or green

```html
<!DOCTYPE html>
<html lang="en">
<head>
<meta charset="utf-8">
<title>Ridgeline Haulage – Business Card</title>
<link href="https://fonts.googleapis.com/css2?family=Lato:wght@400;700&family=Montserrat:wght@600;800&display=swap" rel="stylesheet">
<style>
  :root {
    --page: #2a2a2c;
    --card: #0b0b0c;
    --card-soft: #1a1a1c;
    --texture: #232325;
    --silver-light: #f2f2f2;
    --silver-mid: #b9b9bb;
    --silver-dark: #6d6d70;
    --text: #ffffff;
    --text-dim: #d8d8d8;
    --photo-dark: #2b2b2e;
    --photo-light: #c9cdd1;
  }
  * { box-sizing: border-box; margin: 0; padding: 0; }
  html, body { width: 1200px; height: 800px; overflow: hidden; }
  body {
    background: var(--page);
    font-family: "Lato", sans-serif;
    color: var(--text);
    position: relative;
  }
  .card {
    position: absolute;
    top: 243px;
    width: 550px;
    height: 314px;
    border-radius: 16px;
    overflow: hidden;
    background: var(--card);
    box-shadow: 0 14px 30px rgba(0,0,0,.45);
  }
  .card--front { left: 35px; }
  .card--back { left: 615px; }

  /* Front */
  .front-texture {
    position: absolute; inset: 0;
    background: radial-gradient(circle at 20% 35%, var(--texture), var(--card-soft) 45%, var(--card) 80%);
    clip-path: polygon(0 0, 100% 0, 100% 26%, 0 74%);
  }
  .front-photo {
    position: absolute; top: 0; right: 0;
    width: 280px; height: 150px;
    background: linear-gradient(160deg, #4a4a4d, var(--photo-dark) 55%, #0e0e10);
    clip-path: polygon(22% 0, 100% 0, 100% 58%, 0 100%);
  }
  .front-stripe {
    position: absolute; left: -20px; top: 150px;
    width: 640px; height: 7px;
    background: linear-gradient(90deg, var(--silver-light), var(--silver-mid) 50%, var(--silver-dark));
    transform: rotate(-13.5deg);
    transform-origin: left top;
  }
  .brand {
    position: absolute; left: 34px; top: 62px;
    display: flex; align-items: center; gap: 10px;
  }
  .brand__mark {
    width: 26px; height: 26px; border-radius: 50%;
    background: var(--silver-mid);
  }
  .brand__name {
    font-family: "Lato", sans-serif; font-weight: 700;
    font-size: 20px; line-height: 1.15; color: var(--silver-light);
    letter-spacing: .5px;
  }
  .person {
    position: absolute; left: 34px; bottom: 34px;
  }
  .person__name {
    font-family: "Montserrat", sans-serif; font-weight: 800;
    font-size: 25px; letter-spacing: 1px; color: var(--silver-light);
  }
  .person__role { font-size: 17px; color: var(--text-dim); margin-top: 2px; }
  .contact {
    position: absolute; right: 30px; top: 170px;
    list-style: none; display: flex; flex-direction: column; gap: 6px;
  }
  .contact li { display: flex; align-items: flex-start; gap: 9px; font-size: 14px; color: var(--text-dim); }
  .contact svg { width: 13px; height: 13px; margin-top: 2px; flex: none; fill: var(--silver-mid); }
  .contact .phone { font-size: 19px; font-weight: 700; color: var(--text); }

  /* Back */
  .back-texture {
    position: absolute; inset: 0;
    background: radial-gradient(circle at 75% 55%, var(--texture), var(--card) 75%);
  }
  .back-photo {
    position: absolute; left: 0; top: 70px;
    width: 280px; height: 244px;
    background: linear-gradient(140deg, var(--photo-light), #8e9398 55%, #3a3b3e);
    clip-path: polygon(0 18%, 60% 0, 100% 40%, 100% 100%, 0 100%);
  }
  .services-banner {
    position: absolute; right: 0; top: 0;
    width: 330px; height: 46px;
    background: linear-gradient(90deg, var(--silver-mid), var(--silver-light) 55%, var(--silver-mid));
    clip-path: polygon(0 100%, 12% 0, 100% 0, 100% 100%);
    display: flex; align-items: center; justify-content: flex-end; padding-right: 26px;
  }
  .services-banner h2 {
    font-family: "Montserrat", sans-serif; font-weight: 800;
    font-size: 23px; color: var(--card); letter-spacing: .5px;
  }
  .services {
    position: absolute; right: 22px; top: 58px;
    list-style: none; text-align: right;
  }
  .services li {
    display: flex; justify-content: flex-end; align-items: center; gap: 7px;
    font-size: 15px; line-height: 20px; color: var(--text);
  }
  .services svg { width: 12px; height: 12px; flex: none; }
  .services li.no-tick { padding-right: 19px; }
</style>
</head>
<body>
<svg width="0" height="0" style="position:absolute" aria-hidden="true">
  <symbol id="tick" viewBox="0 0 12 12">
    <circle cx="6" cy="6" r="6" fill="#ffffff"/>
    <path d="M3.2 6.2 5.1 8 8.8 4.2" fill="none" stroke="#0b0b0c" stroke-width="1.7" stroke-linecap="round" stroke-linejoin="round"/>
  </symbol>
</svg>

<section class="card card--front">
  <div class="front-texture"></div>
  <div class="front-photo" role="img" aria-label="Photo of a road train tipper truck at dusk"></div>
  <div class="front-stripe"></div>
  <div class="brand">
    <span class="brand__mark"></span>
    <span class="brand__name">Ridgeline Haulage<br>Pty Ltd</span>
  </div>
  <ul class="contact">
    <li>
      <svg viewBox="0 0 12 12"><path d="M6 0a4 4 0 0 0-4 4c0 3 4 8 4 8s4-5 4-8a4 4 0 0 0-4-4zm0 5.5A1.5 1.5 0 1 1 6 2.5a1.5 1.5 0 0 1 0 3z"/></svg>
      <span>Your Address, City<br>State, Zip 1235</span>
    </li>
    <li>
      <svg viewBox="0 0 12 12"><path d="M2.5 0.5 4.5 2.8 3.4 4.2c.7 1.7 1.9 2.9 3.9 3.9l1.3-1.1 2.4 2-1.3 2C5 10.5 1.5 7 0.6 2z"/></svg>
      <span class="phone">(123) 456-7890</span>
    </li>
    <li>
      <svg viewBox="0 0 12 12"><path d="M0 2h12v8H0zM1 3l5 4 5-4" fill="none" stroke="#b9b9bb" stroke-width="1"/></svg>
      <span>info@yourwebsite.com</span>
    </li>
  </ul>
  <div class="person">
    <p class="person__name">MICHAEL SMITH</p>
    <p class="person__role">Director &amp; Founder</p>
  </div>
</section>

<section class="card card--back">
  <div class="back-texture"></div>
  <div class="back-photo" role="img" aria-label="Photo of a white prime mover with an oversize sign on its bull bar"></div>
  <div class="services-banner"><h2>OUR SERVICES</h2></div>
  <ul class="services">
    <li>Over Size Loads / Hot Shot Loads <svg><use href="#tick"/></svg></li>
    <li>Heavy Vehicle Recovery Services <svg><use href="#tick"/></svg></li>
    <li>Poatable Water Deliveries <svg><use href="#tick"/></svg></li>
    <li>Road Building / Maintenance <svg><use href="#tick"/></svg></li>
    <li>Earthworks <svg><use href="#tick"/></svg></li>
    <li>Sand &amp; Metal Supply &amp; Cartage <svg><use href="#tick"/></svg></li>
    <li>Road Train Tippers <svg><use href="#tick"/></svg></li>
    <li>Road Train Tankers <svg><use href="#tick"/></svg></li>
    <li>Road Train Flat Tops <svg><use href="#tick"/></svg></li>
    <li>Drop Dect Trailers <svg><use href="#tick"/></svg></li>
    <li>Mine Site Accredited <svg><use href="#tick"/></svg></li>
    <li class="no-tick">Equipment &amp; Operators</li>
  </ul>
</section>
</body>
</html>
```